Web design for development company

We would like web, logo and business card designs for a construction and development company in Halifax, Nova Scotia called "R & M Group Developments Limited".

We would like the web design to be professional, and luxurious . The colours should be professional/more mature and easy to read. The website should include: home page, about page, projects, and contact.

The logo design should also be professional in appearance and minimal/not too busy with the company name included. I have attached a few logos that I like for inspiration.

We would like the cards to be double sided with one side being the logo and name of the company. The other side of the card should include the following: logo, company name, name, title, mobile number, office number, fax, email, and website link.

Target Market(s)

general public, potential clients/business partners

Industry/Entity Type

Construction and Development

Coding

Coded - Design and coding required

Number of Pages Required

5+ page

Font styles to use
Serif
Decorative

Requirements
Must have
• the website type i want to receive is coded (the uncoded won't correct to coded on the brief page for some reason) )
Should not have
• playful elements that make the website less professional.Unreadable logos and writing.

```html
<!DOCTYPE html>
<html lang="en">
<head>
<meta charset="utf-8">
<title>R &amp; M Group Developments Limited</title>
<link href="https://fonts.googleapis.com/css2?family=Oswald:wght@300;400;500;600;700&family=Roboto+Condensed:wght@400;700&family=Poppins:wght@400;500&display=swap" rel="stylesheet">
<style>
:root{
  --blue:#1f8ff5;
  --blue-dark:#1479d6;
  --ink:#141414;
  --text:#2a2a2a;
  --muted:#6a6a6a;
  --white:#ffffff;
  --field:#ececec;
  --field-line:#c9c9c9;
  --footer:#1b1b1c;
  --footer-text:#e8e8e8;
}
*{box-sizing:border-box;margin:0;padding:0}
html,body{width:1200px;height:3018px;overflow:hidden}
body{position:relative;background:var(--white);font-family:"Roboto Condensed",sans-serif;color:var(--text)}
.abs{position:absolute}
a{color:inherit;text-decoration:none}
h1,h2,h3,h4{line-height:1.2}

/* brand */
.brand{position:absolute;display:flex;align-items:center;gap:12px;font-family:"Oswald",sans-serif;font-weight:400;color:var(--ink)}
.brand-mark{width:34px;height:34px;background:currentColor}
.brand-name{line-height:1}
.brand-name .n1{display:block;font-size:24px}
.brand-name .n2{display:block;font-size:13px;margin-top:4px;letter-spacing:.3px}

/* header */
.nav{position:absolute;top:32px;left:485px;display:flex;gap:40px;font-family:"Oswald",sans-serif;font-size:14px;font-weight:400;color:var(--ink);line-height:20px}
.nav a.active{color:var(--blue);position:relative}
.nav a.active::after{content:"";position:absolute;left:0;right:0;bottom:-10px;height:2px;background:var(--blue)}
.btn{position:absolute;display:flex;align-items:center;justify-content:space-between;padding:0 8px 0 13px;background:var(--blue);color:var(--white);border-radius:22px;font-family:"Oswald",sans-serif;font-size:15px;box-shadow:0 4px 10px rgba(31,143,245,.35)}
.btn .dot{width:26px;height:26px;border-radius:50%;background:var(--white);display:flex;align-items:center;justify-content:center}
.btn-contact{left:961px;top:23px;width:125px;height:41px;justify-content:center;padding:0}

/* hero */
.hero-photo{position:absolute;left:0;top:0;width:1200px;height:700px;background:linear-gradient(180deg,#d9e6f3 0%,#b7cde4 35%,#6f8fae 60%,#8a9a7e 78%,#9aa59a 100%)}
.hero-title{position:absolute;left:111px;top:222px;font-family:"Oswald",sans-serif;font-weight:700;font-size:72px;line-height:72px;letter-spacing:3px;color:var(--ink)}
.hero-sub{position:absolute;left:111px;top:298px;width:360px;font-family:"Roboto Condensed",sans-serif;font-weight:700;font-size:18px;line-height:25px;color:var(--ink)}
.btn-hero{left:111px;top:363px;width:141px;height:41px}
.arrow{position:absolute;width:59px;height:59px;border:1.5px solid var(--ink);border-radius:50%;display:flex;align-items:center;justify-content:center}

/* section headings */
.sec-bar{position:absolute;width:42px;height:5px;background:var(--blue)}
.sec-title{position:absolute;font-family:"Oswald",sans-serif;font-weight:500;font-size:33px;line-height:40px;letter-spacing:1px;color:var(--ink)}

/* about */
.about-text{position:absolute;left:184px;top:810px;width:410px;font-size:14px;line-height:22.5px;color:var(--text)}
.about-text p+p{margin-top:8px}
.btn-about{left:184px;top:1043px;width:141px;height:41px}
.about-card{position:absolute;left:686px;top:742px;width:384px;height:334px;background:var(--white);border-radius:10px;box-shadow:0 2px 12px rgba(0,0,0,.1)}
.about-frame{position:absolute;left:652px;top:779px;width:386px;height:334px;border:1px solid #3b4a5e;border-radius:10px}
.about-photo{position:absolute;left:666px;top:763px;width:386px;height:332px;border-radius:8px;background:linear-gradient(160deg,#c9c7c0 0%,#8f8c85 50%,#5d5a55 100%)}

/* projects */
.projects{position:absolute;left:0;top:1200px;width:1200px;height:710px;background:var(--blue)}
.projects .sec-title{color:var(--white)}
.projects-sub{position:absolute;left:0;width:1200px;top:146px;text-align:center;color:var(--white);font-weight:700;font-size:15.5px;line-height:22px}
.project{position:absolute;top:227px;width:309px}
.project-photo{height:332px;border-radius:8px 8px 0 0}
.project-name{height:66px;display:flex;align-items:center;justify-content:center;font-family:"Oswald",sans-serif;font-weight:500;font-size:22px;letter-spacing:2px;color:var(--white)}
.project.featured{background:var(--white);border-radius:8px}
.project.featured .project-name{color:var(--ink)}

/* contact */
.contact{position:absolute;left:0;top:1910px;width:1200px;height:700px;background:linear-gradient(180deg,#ffffff 0%,#f1f1f1 30%,#d9d9d8 100%)}
.col-title{position:absolute;font-family:"Oswald",sans-serif;font-weight:400;font-size:21px;color:#3a3a3a}
.detail{position:absolute;left:120px;display:flex;gap:18px}
.detail .ico{flex:none;width:36px;display:flex;justify-content:center}
.detail .label{font-weight:700;font-size:19px;line-height:26px;color:var(--ink)}
.detail .value{font-size:19px;line-height:29px;color:var(--ink)}
.social{position:absolute;width:52px;height:52px;border-radius:50%;background:var(--blue)}
.field{position:absolute;height:55px;background:var(--field);border:1px solid var(--field-line);display:flex;align-items:center;gap:14px;padding-left:16px;font-family:"Poppins",sans-serif;font-size:13px;color:#777}
.field.msg{align-items:flex-start;padding-top:18px}
.btn-submit{left:534px;top:2423px;width:140px;height:41px}
.team-photo{position:absolute;left:855px;top:2403px;width:200px;height:200px;background:linear-gradient(180deg,#d4d4d0 0%,#c9c94a 40%,#3d3d3d 100%);border-radius:4px}

/* footer */
.footer{position:absolute;left:0;top:2606px;width:1200px;height:412px;background:var(--footer)}
.foot-col{position:absolute;top:2710px;font-family:"Oswald",sans-serif;color:var(--footer-text)}
.foot-col .bar{width:42px;height:4px;background:var(--blue)}
.foot-col h4{font-weight:500;font-size:22px;margin-top:8px;color:var(--white)}
.foot-col ul{list-style:none;margin-top:8px}
.foot-col li{font-weight:400;font-size:16.5px;line-height:29px}
.divider{position:absolute;left:111px;top:2932px;width:977px;height:1px;background:#5a5a5a}
.legal{position:absolute;top:2962px;font-family:"Poppins",sans-serif;font-size:13px;line-height:18px;color:var(--white)}
.to-top{position:absolute;left:1102px;top:2907px;width:50px;height:50px;border-radius:50%;background:var(--blue);display:flex;align-items:center;justify-content:center}
</style>
</head>
<body>

<!-- hero -->
<div class="hero-photo" role="img" aria-label="Modern glass office building with cantilevered upper floor under a bright sky"></div>
<svg class="abs" style="left:0;top:600px" width="1200" height="110" viewBox="0 0 1200 110" aria-hidden="true">
  <path d="M0,40 C250,34 470,100 620,92 C800,82 1000,32 1200,38 L1200,110 L0,110 Z" fill="#ffffff"/>
</svg>

<div class="brand" style="left:111px;top:21px">
  <span class="brand-mark"></span>
  <span class="brand-name"><span class="n1">R &amp; M Group</span><span class="n2">Developments Limited</span></span>
</div>

<nav class="nav">
  <a class="active" href="#">HOME</a>
  <a href="#">ABOUT US</a>
  <a href="#">SERVICES</a>
  <a href="#">BLOG</a>
  <a href="#">TESTIMONIALS</a>
</nav>
<a class="btn btn-contact" href="#">Contact Us</a>

<h1 class="hero-title">R &amp; M GROUP</h1>
<p class="hero-sub">Perspiciatis unde omnis iste natus error sit voluptatem accusant iumeaqueillo.</p>
<a class="btn btn-hero" href="#">Get Started <span class="dot"><svg width="10" height="10" viewBox="0 0 10 10"><path d="M3.5 2l3 3-3 3" stroke="#1f8ff5" stroke-width="1.6" fill="none"/></svg></span></a>

<div class="arrow" style="left:23px;top:290px"><svg width="12" height="12" viewBox="0 0 12 12"><path d="M7.5 2.5L4 6l3.5 3.5" stroke="#141414" stroke-width="1.6" fill="none"/></svg></div>
<div class="arrow" style="left:1117px;top:290px"><svg width="12" height="12" viewBox="0 0 12 12"><path d="M4.5 2.5L8 6l-3.5 3.5" stroke="#141414" stroke-width="1.6" fill="none"/></svg></div>

<!-- about -->
<span class="sec-bar" style="left:184px;top:748px"></span>
<h2 class="sec-title" style="left:184px;top:758px">ABOUT US</h2>
<div class="about-text">
  <p>Laukes oloremque laudant iumtotam rem aperiam, eaque ipsa quae ab illo inventore veritatis et quasi architecto beatae vitae dicta sunt explicabo.</p>
  <p>Doloremque laudantium, totam rem aperiam, eaque ipsa quae ab illo inventore veritatis et quasi architecto beatae vitae dicta sunt explicabo. Nemo enim ipsam voluptatem quia voluptas sit aspernatur aut odit aut fugit, sed quia consequuntur magni dolores eos qui ratione voluptatem sequi nesciunt. Neque porro quisquam est, qui dolorem ipsum quia dolor sit amet, consectetur.</p>
</div>
<a class="btn btn-about" href="#">Learn More <span class="dot"><svg width="10" height="10" viewBox="0 0 10 10"><path d="M3.5 2l3 3-3 3" stroke="#1f8ff5" stroke-width="1.6" fill="none"/></svg></span></a>

<div class="about-card"></div>
<div class="about-frame"></div>
<div class="about-photo" role="img" aria-label="Construction workers in hard hats on a concrete staircase inside a building under construction"></div>

<!-- projects -->
<section class="projects">
  <span class="sec-bar" style="left:579px;top:87px;background:#fff"></span>
  <h2 class="sec-title" style="left:0;width:1200px;text-align:center;top:96px">OUR PROJECTS</h2>
  <p class="projects-sub">Laukes oloremque laudant iumtotamrem aperiam eaque ipsa quae abillo inventore veritatis equasi<br>architecto beatae vitae dicta sunt explicabo.</p>

  <div class="project" style="left:111px">
    <div class="project-photo" role="img" aria-label="Glass office building on a paved plaza at dusk" style="background:linear-gradient(160deg,#dfe7ef 0%,#6b7f93 55%,#2d343d 100%)"></div>
    <div class="project-name">ONSECTETUR ADIPISCING</div>
  </div>
  <div class="project featured" style="left:445px">
    <div class="project-photo" role="img" aria-label="Modern multi-storey building with lit windows at sunset" style="background:linear-gradient(160deg,#f3f1ea 0%,#8a7f70 50%,#3b3631 100%)"></div>
    <div class="project-name">VOLUPTATEM ACCUSANTI</div>
  </div>
  <div class="project" style="left:779px">
    <div class="project-photo" role="img" aria-label="Blue glass tower behind green trees and a paved courtyard" style="background:linear-gradient(180deg,#eef2f4 0%,#5f8fb0 45%,#4f7a3c 75%,#a5a8a6 100%)"></div>
    <div class="project-name">LOREMQUE LAUDANTIU</div>
  </div>
</section>

<!-- contact -->
<section class="contact" aria-label="Contact us"></section>
<span class="sec-bar" style="left:579px;top:1998px"></span>
<h2 class="sec-title" style="left:0;width:1200px;text-align:center;top:2007px">CONTACT US</h2>

<h3 class="col-title" style="left:110px;top:2072px">Contact Details</h3>
<h3 class="col-title" style="left:533px;top:2072px">Get In Touch</h3>

<div class="detail" style="top:2140px">
  <span class="ico"><svg viewBox="0 0 26 32" width="26" height="32"><path d="M13 1C6.9 1 2 5.8 2 11.8 2 19.6 13 31 13 31s11-11.4 11-19.2C24 5.8 19.1 1 13 1z" fill="#1f8ff5"/><circle cx="13" cy="11.5" r="4.2" fill="#fff"/></svg></span>
  <div class="value">418 Harbour Crest Road, Halifax, Nova Scotia,<br>Canada. B3H 2Y9</div>
</div>
<div class="detail" style="top:2232px">
  <span class="ico" style="padding-top:10px"><svg viewBox="0 0 26 26" width="26" height="26"><path d="M6 2l4 4.5-2.3 2.6c1.6 3.4 4.2 6 7.6 7.6L17.9 14 22.4 18l-2.6 4.2C11.3 22 3.9 14.6 2 6.3z" fill="#1f8ff5"/></svg></span>
  <div><div class="label">PHONE NUMBER</div><div class="value" style="line-height:26px">902 555 0147</div></div>
</div>
<div class="detail" style="top:2320px">
  <span class="ico" style="padding-top:14px"><svg viewBox="0 0 36 24" width="36" height="24"><rect x="1" y="1" width="34" height="22" fill="#1f8ff5"/><path d="M1 1l17 12L35 1M1 23l12-11M35 23L23 12" stroke="#fff" stroke-width="1.6" fill="none"/></svg></span>
  <div><div class="label">EMAIL</div><div class="value" style="line-height:26px">r&amp;m.group@mail.com</div></div>
</div>

<span class="social" style="left:113px;top:2421px"></span>
<span class="social" style="left:172px;top:2421px"></span>
<span class="social" style="left:231px;top:2421px"></span>
<span class="social" style="left:289px;top:2421px"></span>

<form>
  <label class="field" style="left:534px;top:2119px;width:266px"><svg width="14" height="15" viewBox="0 0 14 15"><circle cx="7" cy="4" r="3.5" fill="#222"/><path d="M0 15c0-4.5 3-7 7-7s7 2.5 7 7z" fill="#222"/></svg>First Name</label>
  <label class="field" style="left:820px;top:2119px;width:266px"><svg width="14" height="15" viewBox="0 0 14 15"><circle cx="7" cy="4" r="3.5" fill="#222"/><path d="M0 15c0-4.5 3-7 7-7s7 2.5 7 7z" fill="#222"/></svg>Last Name</label>
  <label class="field" style="left:534px;top:2192px;width:266px"><svg width="16" height="12" viewBox="0 0 16 12"><rect width="16" height="12" fill="#222"/><path d="M0 0l8 6 8-6" stroke="#ececec" stroke-width="1.3" fill="none"/></svg>Email</label>
  <label class="field" style="left:820px;top:2192px;width:266px"><svg width="15" height="15" viewBox="0 0 26 26"><path d="M6 2l4 4.5-2.3 2.6c1.6 3.4 4.2 6 7.6 7.6L17.9 14 22.4 18l-2.6 4.2C11.3 22 3.9 14.6 2 6.3z" fill="#222"/></svg>Phone</label>
  <label class="field msg" style="left:534px;top:2264px;width:552px;height:135px"><svg width="18" height="15" viewBox="0 0 18 15"><rect x="1" y="1" width="11" height="8" rx="2" fill="none" stroke="#666" stroke-width="1.3"/><rect x="6" y="5" width="11" height="8" rx="2" fill="#ececec" stroke="#666" stroke-width="1.3"/></svg>Message</label>
</form>
<a class="btn btn-submit" href="#">Submit <span class="dot"><svg width="10" height="10" viewBox="0 0 10 10"><path d="M3.5 2l3 3-3 3" stroke="#1f8ff5" stroke-width="1.6" fill="none"/></svg></span></a>

<div class="team-photo" role="img" aria-label="Team of engineers in hi-vis jackets and hard hats reviewing plans"></div>

<!-- footer -->
<svg class="abs" style="left:0;top:2550px" width="1200" height="60" viewBox="0 0 1200 60" aria-hidden="true">
  <path d="M0,58 C200,50 480,20 600,4 C720,20 1000,52 1200,56 L1200,60 L0,60 Z" fill="#1b1b1c"/>
</svg>
<footer class="footer"></footer>

<div class="brand" style="left:114px;top:2756px;color:#ffffff">
  <span class="brand-mark" style="width:44px;height:44px"></span>
  <span class="brand-name"><span class="n1" style="font-size:31px">R &amp; M Group</span><span class="n2" style="font-size:16px">Developments Limited</span></span>
</div>

<div class="foot-col" style="left:485px">
  <div class="bar"></div><h4>QUICK LINKS</h4>
  <ul><li>Home</li><li>About Us</li><li>Services</li><li>Blog</li><li>Testimonials</li></ul>
</div>
<div class="foot-col" style="left:707px">
  <div class="bar"></div><h4>LINKS</h4>
  <ul><li>Frequently Asked Questions</li><li>Terms &amp; Conditions</li><li>Privacy Policy</li><li>Site Map</li></ul>
</div>
<div class="foot-col" style="left:997px">
  <div class="bar"></div><h4>SUPPORT</h4>
  <ul><li>Copyright</li><li>Legal</li><li>Privacy</li><li>Accessibility</li><li>Sitemap</li></ul>
</div>

<div class="divider"></div>
<a class="to-top" href="#"><svg width="12" height="12" viewBox="0 0 12 12"><path d="M2.5 7.5L6 4l3.5 3.5" stroke="#141414" stroke-width="1.6" fill="none"/></svg></a>
<p class="legal" style="left:111px">Copyrights ©2021. All Rights Reserved</p>
<p class="legal" style="left:900px">Privacy Policy <span style="color:var(--blue);margin:0 12px">|</span> Site Map</p>

</body>
</html>
```